Briarwick Dale Half Marathon 2015

I am in need of a 2 sided promotional print postcard for our half marathon held in March. The print is distributed in October.

Must include running stick figure, Corlandt Vee Bridge and lighthouse in design. These elements can be seen in the uploaded design from last year. Also, the Stonemill Striders Logo and Ashgrove logo must be on it.

Saturday, March 21st at 9:30am
Register on RACELY.example
Register before end of 2014 and recieve $5 off registration - Use coupon code BK7948

Back of the post card to include details:

Registration fee $60 until 3/13/14, race day $70
Race start/finish is walking distance from the train -Valeway Coastal Line to Millbrook Station
Finisher Goodie bag
LS technical shirt
Electronic timing
NRFB Certified course
Water and Quenchix fluid stations
CASH awards to top 3 overall male and female finishers
Awards and prizes to top category finishers
Each finisher will receive a 2014 Briarwick Dale Half Marathon medal, sponsored by Ashgrove Memorial Hospital Center

Target Market(s)

These are males and females ages 21-55

Industry/Entity Type

Electronic

Colors
33a6d7
34b8a4
faee3f
add136
3176b5
f04a50

Requirements
Must have
• 2 logos
name - Briarwick Dale Half Marathon
date
www.stonemillstriders.example
2 sided with detailed info on back and general info on front

```html
<!DOCTYPE html>
<html lang="en">
<head>
<meta charset="utf-8">
<title>Briarwick Dale Half Marathon – Postcard Back</title>
<link rel="stylesheet" href="https://fonts.googleapis.com/css2?family=Alfa+Slab+One&display=swap">
<style>
  :root {
    --teal: #34b8a4;
    --yellow: #faee3f;
    --red: #f04a50;
    --blue: #3176b5;
    --green: #add136;
    --paper: #ffffff;
  }
  * { margin: 0; padding: 0; box-sizing: border-box; }
  html, body { width: 1200px; height: 776px; overflow: hidden; background: var(--paper); }
  .postcard { position: relative; width: 1200px; height: 776px; }
  .postcard svg { display: block; }
  .copy { font-family: "Alfa Slab One", "Rockwell", serif; }
  .fee { fill: var(--yellow); font-size: 40px; }
  .transit { fill: var(--yellow); font-size: 28px; }
  .perks { fill: var(--blue); font-size: 22px; }
  .awards { fill: var(--red); font-size: 22px; }
  .medal { fill: var(--green); font-size: 19px; }
</style>
</head>
<body>
<main class="postcard">
  <svg width="1200" height="776" viewBox="0 0 1200 776">
    <defs>
      <linearGradient id="crowdTone" x1="0" y1="0" x2="1" y2="1">
        <stop offset="0" stop-color="#f04a50"/>
        <stop offset="0.45" stop-color="#f3634f"/>
        <stop offset="1" stop-color="#f04a50"/>
      </linearGradient>
      <linearGradient id="bridgeTone" x1="0" y1="0" x2="1" y2="0">
        <stop offset="0" stop-color="#faee3f" stop-opacity="0.9"/>
        <stop offset="1" stop-color="#faee3f" stop-opacity="0.35"/>
      </linearGradient>
    </defs>

    <path class="sky" fill="var(--teal)" d="M0 0H1005V193H1200V300H0Z"/>

    <path class="river" fill="var(--yellow)"
      d="M0 318 L140 322 L300 326 L420 324 L520 314 L640 308 L760 306 L880 300 L1000 296 L1100 292 L1200 288 V340 H797 V345 H0Z"/>

    <path role="img" aria-label="Yellow silhouette of the Corlandt Vee Bridge spanning the river"
      fill="url(#bridgeTone)" d="M0 312 L80 300 L190 268 L250 262 L330 276 L420 300 L480 318 L480 345 H0Z"/>

    <path role="img" aria-label="Red and yellow duotone photo of a crowd of runners at the race start"
      fill="url(#crowdTone)" d="M0 345H797V670H518V776H0Z"/>

    <path class="highlight" fill="var(--yellow)"
      d="M205 398 Q240 382 300 390 Q360 380 420 392 Q500 380 560 394 Q640 384 690 402 Q708 440 694 480 Q706 508 660 514 Q560 520 460 514 Q340 522 250 516 Q208 506 212 470 Q196 432 205 398Z"/>
    <path class="highlight" fill="var(--yellow)"
      d="M30 526 Q90 510 200 516 Q330 506 460 520 Q600 520 720 548 Q792 560 788 590 Q770 612 700 608 Q600 616 480 610 Q340 612 220 600 Q110 596 48 578 Q18 556 30 526Z"/>

    <text class="copy fee" transform="rotate(-2 82 100)">
      <tspan x="82" y="100" textLength="898" lengthAdjust="spacingAndGlyphs">Registration fee $60 until 3/13/14,</tspan>
      <tspan x="82" y="146" textLength="300" lengthAdjust="spacingAndGlyphs">race day $70</tspan>
    </text>

    <text class="copy transit" transform="rotate(3 395 214)">
      <tspan x="395" y="214" textLength="650" lengthAdjust="spacingAndGlyphs">Race start/finish is walking distance</tspan>
      <tspan x="392" y="241" textLength="712" lengthAdjust="spacingAndGlyphs">from the train -Valeway Coastal Line</tspan>
      <tspan x="389" y="268" textLength="375" lengthAdjust="spacingAndGlyphs">to Millbrook Station</tspan>
    </text>

    <text class="copy perks">
      <tspan x="217" y="417" textLength="266" lengthAdjust="spacingAndGlyphs">Finisher Goodie bag</tspan>
      <tspan x="217" y="441" textLength="235" lengthAdjust="spacingAndGlyphs">LS technical shirt</tspan>
      <tspan x="217" y="464" textLength="216" lengthAdjust="spacingAndGlyphs">Electronic timing</tspan>
      <tspan x="217" y="487" textLength="300" lengthAdjust="spacingAndGlyphs">NRFB Certified course</tspan>
      <tspan x="217" y="506" textLength="463" lengthAdjust="spacingAndGlyphs">Water and Quenchix fluid stations</tspan>
    </text>

    <text class="copy awards" transform="rotate(3 40 541)">
      <tspan x="40" y="541" textLength="742" lengthAdjust="spacingAndGlyphs">CASH awards to top 3 overall male and female finishers</tspan>
      <tspan x="40" y="562" textLength="582" lengthAdjust="spacingAndGlyphs">Awards and prizes to top category finishers</tspan>
    </text>

    <text class="copy medal" transform="rotate(-3.2 75 662)">
      <tspan x="75" y="662" textLength="278" lengthAdjust="spacingAndGlyphs">Each finisher will receive</tspan>
      <tspan x="75" y="681" textLength="540" lengthAdjust="spacingAndGlyphs">a 2014 Briarwick Dale Half Marathon medal,</tspan>
      <tspan x="75" y="700" textLength="172" lengthAdjust="spacingAndGlyphs">sponsored by</tspan>
      <tspan x="78" y="719" textLength="436" lengthAdjust="spacingAndGlyphs">Ashgrove Memorial Hospital Center</tspan>
    </text>
  </svg>
</main>
</body>
</html>
```